Orvessa Develoipment and Management Corp Web Design Project

Website... Based on logo. Update forthcoming....
Updates

Reason: Extended to include recently completed logo design.

Target Market(s)

Financiers, investors, public officials, and landowners.

Industry/Entity Type

Management

Requirements
Should not have
• No palm trees, mayan ruins, or other Caribbean references.

```html
<!DOCTYPE html>
<html lang="en">
<head>
<meta charset="utf-8">
<title>Orvessa Develoipment and Management Corp</title>
<link href="https://fonts.googleapis.com/css2?family=Raleway:wght@400;500;600&family=Ubuntu:ital,wght@0,400;0,500;1,400&display=swap" rel="stylesheet">
<style>
:root{
  --green:#a3bb36;
  --navy:#3b4d6b;
  --text:#555;
  --muted:#8a8a8a;
  --band:#efefef;
  --footer:#151716;
  --footer-deep:#0c0d0d;
  --white:#fff;
}
*{margin:0;padding:0;box-sizing:border-box}
html,body{width:993px;height:1200px;overflow:hidden}
body{position:relative;background:#fafafa;font-family:'Raleway',sans-serif;color:var(--text)}
.abs{position:absolute}

/* header */
.site-header{left:0;top:0;width:993px;height:63px;background:var(--white)}
.brand{left:108px;top:16px;display:flex;align-items:center;gap:7px}
.brand-mark{width:24px;height:24px;background:var(--green)}
.brand-name{font-family:'Raleway',sans-serif;font-weight:600;font-size:22px;color:var(--green);letter-spacing:1px}
.main-nav a{position:absolute;top:25px;font-size:13.5px;color:#666;text-decoration:none}
.main-nav a.current{color:#333;text-decoration:underline;text-underline-offset:3px}

/* hero */
.hero{left:0;top:63px;width:993px;height:367px;background:linear-gradient(180deg,#56647a 0%,#6a7080 45%,#7a6459 70%,#5d5148 100%)}
.hero-edge{left:0;top:430px;width:993px;height:4px;background:var(--navy)}
.hero-title{left:0;top:150px;width:993px;text-align:center;font-family:'Raleway',sans-serif;font-weight:500;font-size:40px;line-height:48px;color:var(--white)}
.hero-lead{left:0;top:214px;width:993px;text-align:center;font-size:15.5px;line-height:25px;color:var(--white)}
.btn-learn{left:416px;top:309px;width:161px;height:44px;border:3px solid var(--white);border-radius:5px;background:var(--green);color:var(--white);font-weight:600;font-size:17.5px;display:flex;align-items:center;justify-content:center}

/* section titles */
.section-title{font-size:23px;font-weight:400;color:#666;display:flex;align-items:flex-end;gap:6px}
.section-title b{font-weight:500;color:#444}
.tri{width:0;height:0;border-left:10px solid transparent;border-bottom:10px solid var(--green);margin-bottom:5px}
.tri.sm{border-left-width:9px;border-bottom-width:9px;margin-bottom:4px}

.welcome-text{left:107px;top:514px;width:480px;font-size:13px;line-height:20.7px;color:var(--muted)}

.tweet{left:687px;width:150px;display:flex;gap:10px;font-family:'Ubuntu',sans-serif}
.tweet-icon{width:17px;height:17px;border:1.5px solid #3aa8dc;border-radius:50%;flex:none;margin-top:2px}
.tweet p{font-size:6.3px;line-height:10px;color:#888}
.tweet em{display:block;font-size:6.5px;color:var(--green);margin-top:1px}

.gallery-item{top:679px;width:183px;height:171px}
.gallery-overlay{left:0;top:0;width:183px;height:171px;background:rgba(40,65,105,.8);color:var(--white);font-family:'Ubuntu',sans-serif;font-size:11.5px;text-align:center;padding-top:58px}
.gallery-overlay svg{display:block;margin:10px auto 0}

/* newsletter */
.newsletter{left:0;top:884px;width:993px;height:68px;background:var(--band)}
.newsletter-text{left:161px;top:900px;font-family:'Ubuntu',sans-serif;font-size:12.4px;line-height:19px;color:#666}
.newsletter-text b{font-weight:500;color:#444}
.email-field{left:488px;top:907px;width:244px;height:24px;border:1.5px solid #ccc;border-radius:3px;background:var(--white);font-family:'Ubuntu',sans-serif;font-style:italic;font-size:9.5px;color:#999;padding:6px 0 0 17px}
.btn-subscribe{left:745px;top:907px;width:86px;height:24px;border:1.5px solid #b9c1cf;border-radius:3px;background:var(--navy);color:var(--white);font-family:'Ubuntu',sans-serif;font-style:italic;font-size:9.5px;display:flex;align-items:center;justify-content:center}

/* footer */
.site-footer{left:0;top:952px;width:993px;height:214px;background:var(--footer)}
.footer-bottom{left:0;top:1166px;width:993px;height:34px;background:var(--footer-deep);color:#888;font-family:'Ubuntu',sans-serif;font-size:10px;text-align:center;line-height:34px}
.footer-title{top:981px;font-size:15.7px;font-weight:400;color:var(--white);display:flex;align-items:flex-end;gap:6px}
.footer-title .tri{border-left-width:8px;border-bottom-width:8px;margin-bottom:3px}
.field{left:108px;width:126px;background:#e6e6e6;font-family:'Ubuntu',sans-serif;font-style:italic;font-size:6.5px;color:#999;padding:4px 0 0 9px}
.btn-submit{left:108px;top:1130px;width:33px;height:12px;background:var(--navy);color:var(--white);font-family:'Ubuntu',sans-serif;font-size:7px;display:flex;align-items:center;justify-content:center}
.quick-links a{position:absolute;left:336px;font-family:'Ubuntu',sans-serif;font-size:10.8px;color:var(--white);text-decoration:none}
.news-item{left:523px;width:151px;display:flex;gap:6px}
.news-date{width:30px;height:28px;background:var(--white);border-radius:2px;overflow:hidden;flex:none;text-align:center;font-family:'Ubuntu',sans-serif}
.news-date span{display:block;background:var(--navy);color:var(--white);font-size:7px;line-height:10px}
.news-date strong{display:block;font-weight:400;font-size:11px;line-height:17px;color:var(--navy)}
.news-item p{font-family:'Ubuntu',sans-serif;font-size:5.5px;line-height:8.2px;color:var(--white);padding-top:3px}
.news-rule{left:523px;width:151px;height:1px;background:#4a5880}
.view-all{left:524px;top:1127px;font-family:'Ubuntu',sans-serif;font-style:italic;font-size:7.5px;color:#ccc;text-decoration:underline}
.social a{position:absolute;left:751px;width:90px;font-family:'Ubuntu',sans-serif;font-size:10.8px;color:var(--white);text-decoration:none}
.social i{position:absolute;left:73px;top:0;width:14px;height:14px}
</style>
</head>
<body>

<header class="site-header abs">
  <div class="brand abs"><span class="brand-mark"></span><span class="brand-name">ORVESSA</span></div>
  <nav class="main-nav">
    <a class="current" style="left:508px">Home</a>
    <a style="left:563px">Services</a>
    <a style="left:631px">Our Team</a>
    <a style="left:709px">Insight Articles</a>
    <a style="left:817px">Contact Us</a>
  </nav>
</header>

<section class="hero abs" role="img" aria-label="Blurred panoramic photo of a city skyline with red rooftops under a cloudy sky"></section>
<div class="hero-edge abs"></div>
<h1 class="hero-title abs">SIMPLE. GOOD DESIGN.</h1>
<p class="hero-lead abs">This is sample text only. Lorem ipsum dolor sit amet,<br>consectetur adipisicing elit, sed do eiusmod.</p>
<div class="btn-learn abs">LEARN MORE</div>

<h2 class="section-title abs" style="left:108px;top:472px"><span class="tri"></span>Welcome to <b>Orvessa</b></h2>
<p class="welcome-text abs">Culpa qui officia deserunt mollit anim id est laborum. Sed ut perspiciatis unde omnis iste natus error sit voluptatem accusantium doloremque laudantium, totam rem aperiam, eaque ipsa quae ab illo inventore veritatis et quasi archi tecto beatae vitae dicta sunt explicabo.</p>

<h2 class="section-title abs" style="left:687px;top:472px"><span class="tri"></span>Latest <b>Tweets</b></h2>
<div class="tweet abs" style="top:518px"><span class="tweet-icon"></span><p>Eiusmod tempor incididunt ut labore<br>et dolore magna aliqua.<em>About 3 hours ago</em></p></div>
<div class="tweet abs" style="top:566px"><span class="tweet-icon"></span><p>Ut enim ad minim veniam, quis<br>nostrud exercitation.<em>About 4 hours ago</em></p></div>

<h2 class="section-title abs" style="left:108px;top:638px;font-size:17.5px"><span class="tri sm"></span>Our <b>Gallery</b></h2>
<div class="gallery-item abs" style="left:108px;background:linear-gradient(180deg,#5a6e86,#34465e)" role="img" aria-label="Photo of a rocky coastline and sea">
  <div class="gallery-overlay abs">Sample picture only
    <svg width="70" height="24" viewBox="0 0 70 24" fill="none" stroke="#fff" stroke-width="2.2">
      <path d="M14 3H3v18h18V10"/><path d="M12 12L21 3M15 3h6v6"/>
      <circle cx="53" cy="9" r="6.5"/><path d="M58 14l7 7" stroke-width="3.5"/>
    </svg>
  </div>
</div>
<div class="gallery-item abs" style="left:306px;background:linear-gradient(180deg,#b8b3a0,#6b645a 55%,#3a3630)" role="img" aria-label="Sepia photo of a Paris street with a tall iron tower and bare trees"></div>
<div class="gallery-item abs" style="left:504px;background:linear-gradient(180deg,#7fa4d4 0%,#d9dce0 30%,#6f9a48 60%,#3f5e2a 100%)" role="img" aria-label="Photo of a white castle above terraced green gardens"></div>
<div class="gallery-item abs" style="left:703px;background:linear-gradient(90deg,#2c3340,#4a4f55 50%,#c9b9a1)" role="img" aria-label="Photo of tall glass office towers"></div>

<section class="newsletter abs"></section>
<p class="newsletter-text abs">Sign Up to our Newsletter to receive daily news<br>and updates from <b>Orvessa</b></p>
<div class="email-field abs">Enter your Email</div>
<div class="btn-subscribe abs">Subscribe</div>

<footer class="site-footer abs"></footer>
<h3 class="footer-title abs" style="left:106px"><span class="tri"></span>Contact Form</h3>
<h3 class="footer-title abs" style="left:329px"><span class="tri"></span>Quick Links</h3>
<h3 class="footer-title abs" style="left:524px"><span class="tri"></span>Latest News</h3>
<h3 class="footer-title abs" style="left:752px"><span class="tri"></span>Connect with Us</h3>

<div class="field abs" style="top:1027px;height:17px">Enter your Email</div>
<div class="field abs" style="top:1051px;height:17px">Subject</div>
<div class="field abs" style="top:1075px;height:48px">Your Message</div>
<div class="btn-submit abs">Submit</div>

<nav class="quick-links">
  <a style="top:1026px">Home</a>
  <a style="top:1045px">Services</a>
  <a style="top:1064px">Our Team</a>
  <a style="top:1083px">Insight Articles</a>
  <a style="top:1102px">Contact Us</a>
</nav>

<div class="news-item abs" style="top:1030px"><div class="news-date"><span>Aug</span><strong>15</strong></div><p>Eiusmod tempor incididunt ut labore et dolore magna aliqua. Ut enim ad minim veniam, quis nostrud exercitation ullam...[Read More]</p></div>
<div class="news-rule abs" style="top:1067px"></div>
<div class="news-item abs" style="top:1081px"><div class="news-date"><span>Aug</span><strong>24</strong></div><p>Eiusmod tempor incididunt ut labore et dolore magna aliqua. Ut enim ad minim veniam, quis nostrud exercitation ullam...[Read More]</p></div>
<div class="news-rule abs" style="top:1120px"></div>
<span class="view-all abs">View All</span>

<nav class="social">
  <a style="top:1027px">Circlebook<i style="background:#3b5a98"></i></a>
  <a style="top:1049px">Chirpline<i style="background:#2aa9e0"></i></a>
  <a style="top:1072px">Searchplus<i style="background:#d7452f"></i></a>
  <a style="top:1094px">Linkwork<i style="background:#1a7bb9"></i></a>
</nav>

<div class="footer-bottom abs">Copyright©orvessa2014. All Rights Reserved</div>

</body>
</html>
```